Boat business cards

I'm looking for business cards with the two logos I've attached. I don't have an specific idea in mind and open to anything. All the usual info will be on the card. Name, position in company, nr, email, address, ect. The company rents out these two boats for charters and fishing.

```html
<!DOCTYPE html>
<html lang="en">
<head>
<meta charset="utf-8">
<title>Polar Tide Business Cards</title>
<link href="https://fonts.googleapis.com/css2?family=Open+Sans:wght@400;600&display=swap" rel="stylesheet">
<style>
  :root {
    --stage: #d9d9d9;
    --card-dark: #161616;
    --card-light: #ffffff;
    --ink: #2a2a2a;
    --gold: #a98b5f;
    --muted: #6a6a6a;
  }
  html, body {
    margin: 0;
    padding: 0;
    overflow: hidden;
  }
  .canvas {
    position: relative;
    width: 1200px;
    height: 675px;
    background: var(--stage);
    font-family: "Open Sans", Arial, sans-serif;
    overflow: hidden;
  }
  .card {
    position: absolute;
    top: 194px;
    width: 500px;
    height: 286px;
    border-radius: 16px;
    box-shadow: 0 10px 24px rgba(0,0,0,0.22);
    overflow: hidden;
  }
  .card-front {
    left: 70px;
    background: var(--card-dark);
    display: flex;
    align-items: center;
    justify-content: center;
  }
  .card-back {
    left: 630px;
    background: var(--card-light);
  }
  .brand-name {
    font-weight: 600;
    letter-spacing: 1px;
    margin: 0;
  }
  .card-front .brand-name {
    color: #ffffff;
    font-size: 38px;
  }
  .card-back .brand-name {
    position: absolute;
    top: 44px;
    left: 0;
    width: 100%;
    text-align: center;
    color: var(--card-dark);
    font-size: 28px;
  }
  .rule {
    position: absolute;
    top: 122px;
    left: 28px;
    width: 444px;
    height: 1px;
    background: var(--gold);
  }
  .contact {
    position: absolute;
    top: 150px;
    left: 28px;
    display: grid;
    grid-template-columns: 180px 150px;
    row-gap: 10px;
    column-gap: 12px;
    font-size: 12px;
    color: var(--ink);
  }
  .contact-item {
    display: flex;
    align-items: center;
    gap: 6px;
    white-space: nowrap;
  }
  .contact-item svg {
    width: 12px;
    height: 12px;
    flex: none;
  }
  .person {
    position: absolute;
    right: 28px;
    bottom: 30px;
    padding-left: 14px;
    border-left: 1px solid var(--gold);
    height: 110px;
    display: flex;
    flex-direction: column;
    justify-content: flex-end;
  }
  .person-name {
    color: var(--gold);
    font-size: 20px;
    margin: 0;
    line-height: 1.1;
  }
  .person-role {
    color: var(--muted);
    font-size: 11px;
    margin: 0;
  }
</style>
</head>
<body>
<div class="canvas">
  <section class="card card-front">
    <p class="brand-name">Polar Tide</p>
  </section>

  <section class="card card-back">
    <p class="brand-name">Polar Tide</p>
    <div class="rule"></div>
    <div class="contact">
      <div class="contact-item">
        <svg viewBox="0 0 12 12"><path d="M6 1a3.5 3.5 0 0 0-3.5 3.5C2.5 7 6 11 6 11s3.5-4 3.5-6.5A3.5 3.5 0 0 0 6 1zm0 4.8a1.3 1.3 0 1 1 0-2.6 1.3 1.3 0 0 1 0 2.6z" fill="var(--gold)"/></svg>
        <span>address Line 1 &amp; Line 2</span>
      </div>
      <div class="contact-item">
        <svg viewBox="0 0 12 12"><path d="M3 1.5l1.8 2.2-1 1.1a6 6 0 0 0 3.4 3.4l1.1-1L10.5 9 9.4 10.5C5 10.2 1.8 7 1.5 2.6z" fill="var(--gold)"/></svg>
        <span>000 000 0000</span>
      </div>
      <div class="contact-item">
        <svg viewBox="0 0 12 12"><rect x="1" y="2.5" width="10" height="7" rx="1" fill="var(--gold)"/><path d="M1.5 3l4.5 3.3L10.5 3" fill="none" stroke="#fff" stroke-width="0.9"/></svg>
        <span>hello@polartide.co.in</span>
      </div>
      <div class="contact-item">
        <svg viewBox="0 0 12 12"><circle cx="6" cy="6" r="4.8" fill="none" stroke="var(--gold)" stroke-width="1"/><path d="M1.2 6h9.6M6 1.2c-2.4 2.6-2.4 7 0 9.6M6 1.2c2.4 2.6 2.4 7 0 9.6" fill="none" stroke="var(--gold)" stroke-width="0.8"/></svg>
        <span>polartide.com</span>
      </div>
    </div>
    <div class="person">
      <p class="person-name">NAME</p>
      <p class="person-role">Designation</p>
    </div>
  </section>
</div>
</body>
</html>
```